Zentrova - Creative Automation

We are a software house for Audio Visual Systems integration/automation and home automation. we develop innovative software to automate a variety of devices mainly related to audio visuals and we design touch panel user interfaces to control these systems.

We would like to see designs that stick to our colours and theme, which you can find on our webpage www.zentrova.com.au

The final design should communicate touch panels, innovation, software and automation.

Industry/Entity Type

Software

Requirements
Must have
• The business card must show the following information:
Name example : Derek Malloway
Qualification example: B Eng ICT(CompSys) Dip EngPrac
Title example : Control Systems Programmer
Mobile Phone, Company phone, Email address ,Company website

```html
<!DOCTYPE html>
<html lang="en">
<head>
<meta charset="utf-8">
<title>Zentrova – Business Card</title>
<link href="https://fonts.googleapis.com/css2?family=Open+Sans:wght@400;600;700&display=swap" rel="stylesheet">
<style>
  :root {
    --page-bg: #2b2b2d;
    --card-white: #f4f4f4;
    --card-white-edge: #dcdcdc;
    --card-slate: #4f5f6c;
    --card-slate-dark: #3f4d59;
    --brand-blue: #1f6fb8;
    --brand-green: #14985a;
    --ink-dark: #2a2a2a;
    --ink-mid: #4a4a4a;
    --tag-grey: #6c6c6c;
  }
  * { box-sizing: border-box; margin: 0; padding: 0; }
  html, body {
    width: 1200px; height: 900px; overflow: hidden;
    background: var(--page-bg);
    font-family: "Open Sans", Arial, sans-serif;
  }
  .stage {
    width: 1200px; height: 900px;
    display: flex; align-items: center; justify-content: center; gap: 40px;
  }
  .card {
    width: 540px; height: 309px;
    border-radius: 22px;
    position: relative;
    overflow: hidden;
    box-shadow: 0 14px 34px rgba(0,0,0,0.45);
  }
  /* back of card */
  .card-back {
    background: linear-gradient(160deg, var(--card-slate) 0%, var(--card-slate-dark) 100%);
    display: flex; align-items: center; justify-content: center;
  }
  .brand {
    display: flex; flex-direction: column; align-items: flex-start;
  }
  .brand-row { display: flex; align-items: center; gap: 14px; }
  .brand-square {
    width: 38px; height: 38px; background: var(--brand-green); border-radius: 4px;
  }
  .brand-name {
    font-weight: 700; color: var(--brand-blue); line-height: 1;
  }
  .brand-tagline {
    font-weight: 700; line-height: 1; margin-top: 6px; align-self: flex-end;
  }
  .card-back .brand-name { font-size: 54px; }
  .card-back .brand-tagline { font-size: 13px; color: #c8d0d6; }

  /* front of card */
  .card-front {
    background: linear-gradient(135deg, #ffffff 0%, var(--card-white) 55%, var(--card-white-edge) 100%);
  }
  .card-front .brand {
    position: absolute; left: 34px; top: 150px;
  }
  .card-front .brand-square { width: 30px; height: 30px; }
  .card-front .brand-name { font-size: 40px; }
  .card-front .brand-tagline { font-size: 10px; color: var(--tag-grey); }

  .contact {
    position: absolute; left: 272px; top: 36px; width: 250px;
    color: var(--ink-mid);
  }
  .person-name { font-size: 19px; color: var(--brand-blue); font-weight: 400; }
  .qualification { font-size: 10.5px; font-weight: 700; color: var(--ink-dark); margin-top: 2px; }
  .role { font-size: 13px; color: var(--ink-mid); }
  .lines { list-style: none; margin-top: 30px; font-size: 13px; line-height: 1.45; }
  .lines .key { display: inline-block; width: 18px; color: var(--brand-blue); }
  .address { margin-top: 12px; font-size: 13px; line-height: 1.45; }
  .website { margin-top: 14px; font-size: 13px; }
</style>
</head>
<body>
<main class="stage">
  <section class="card card-back" aria-label="Card back">
    <div class="brand">
      <div class="brand-row">
        <span class="brand-square"></span>
        <span class="brand-name">Zentrova</span>
      </div>
      <span class="brand-tagline">Creative Automation</span>
    </div>
  </section>

  <section class="card card-front" aria-label="Card front">
    <div class="brand">
      <div class="brand-row">
        <span class="brand-square"></span>
        <span class="brand-name">Zentrova</span>
      </div>
      <span class="brand-tagline">Creative Automation</span>
    </div>

    <div class="contact">
      <h1 class="person-name">Derek Malloway</h1>
      <p class="qualification">B Eng ICT(CompSys) Dip EngPrac</p>
      <p class="role">Control Systems Programmer</p>
      <ul class="lines">
        <li><span class="key">M</span>0412 555 018</li>
        <li><span class="key">P</span>0255 501 742</li>
        <li><span class="key">E</span>derekmalloway@zentrova.com.au</li>
      </ul>
      <p class="address">12 Millbrook Lane<br>Glenhaven, NSW, 2156</p>
      <p class="website">www.zentrova.com.au</p>
    </div>
  </section>
</main>
</body>
</html>
```